Pellman Haulers collage project

i needed A brochure or a paper that folds in (3 front back middle ) etc.

Look for my Logo ******* Kestrel
Look for my buisness card ****** Kestrel pellman haulers
I Need white black yellow colors to match my logos and buisness cards
Please

I need Energy
modern ,COLLAGE, ,Alive ,very modern ..the future of buisness
I have more pictures to download but brief forge wont let me
send me your email i will email rest of pictures to you Alot of pictures i want a collage
Energy
Modern
Futuristic

Kestrel
PellmanHaulers

PellmanHaulers.example
Follow us on ig fb google +,youtube
Serving Atlanta and surroundings areas

Residential/commercial
Construction jobsites
Residential remodels
Clean outs
Weekly services
We make it simple just call for your next project or visit us online
Updates

I was interested in a collage Examples are being uploaded now ....

Target Market(s)

Construction , and everyone
Residential /commercial

Industry/Entity Type

Construction Company

Requirements
Must have
• Kestrel
• Pellman Haulers
• ~Residential/Commercial
• ~Construction Jobsites
• ~Residential Remodels
• ~Clean Outs / Forclosure
• ~Yard Waste Removal
• ~Weekly Services / Daily
• ~Dump Trailers / Roll Offs
• Roofing project? Our specialty...... multiple roofs in 1 day? No problem
• You can depend on Kestrel to be their for you on time: For Delivery and Pick up.
• Contractors /Roofing companies/Buisness owners/Homeowners we can work
• Exclusively with you to fit your needs ~whether you need weekly services ,daily or just need us 1 time ,No problem
• We make it simple just call for your next project or visit us online
• PellmanHaulers.example
• CALL NOW 555 314 2790
• Follow us on ig fb google +,youtube
• Serving Atlanta and surroundings areas
• QTC (logo) Wendo board (logo)
Nice to have
• I would like to have an atlanta custom back ground and not all but i want to use alot of the pictures
• And a modern
• Some pictures are just an idea like my buisness card
• Please proof read words
• And organize however you feel fits the flyer best
• Any ideas you have or something i should delete let me know and please do reorganize
Should not have
• Should not have my name from.my buisness card or my number

```html
<!DOCTYPE html>
<html lang="en">
<head>
<meta charset="utf-8">
<title>Kestrel Pellman Haulers – Flyer</title>
<link href="https://fonts.googleapis.com/css2?family=Russo+One&family=Roboto:wght@400&family=Roboto+Condensed:wght@400;700&family=Lato:wght@400;700&display=swap" rel="stylesheet">
<style>
  :root{
    --yellow:#f2c200;
    --gold:#e2b43a;
    --black:#0b0b0b;
    --ink:#1d1d1d;
    --paper:#ffffff;
    --mist:#ececec;
    --stage:#dfe3e6;
    --badge:#1d5f93;
  }
  *{margin:0;padding:0;box-sizing:border-box}
  html,body{width:1200px;height:1200px;overflow:hidden;background:var(--stage)}
  .flyer{position:absolute;left:165px;top:37px;width:870px;height:1125px;background:var(--paper);overflow:hidden;font-family:"Lato",sans-serif;color:var(--ink)}
  .brand{position:absolute;left:229px;top:27px;height:87px;display:flex;align-items:center;gap:12px}
  .brand-square{width:87px;height:87px;background:var(--yellow);border:1px solid #8a6d00}
  .brand-name{display:flex;flex-direction:column;line-height:1}
  .brand-name .main{font-family:"Russo One",sans-serif;font-size:44px;color:var(--black);letter-spacing:1px}
  .brand-name .sub{font-family:"Lato",sans-serif;font-size:27px;color:var(--black);letter-spacing:3px;margin-top:4px}
  .collage{position:absolute;left:0;top:123px;width:870px;height:495px}
  .services{position:absolute;left:0;top:621px;width:870px;height:46px;background:var(--yellow);text-align:center;font-family:"Roboto Condensed",sans-serif;font-weight:700;font-size:14px;line-height:20px;padding-top:3px;color:var(--black)}
  .services .dot{margin:0 6px}
  .headline{position:absolute;left:0;top:670px;width:870px;height:139px;background:linear-gradient(90deg,#000 0%,#1a1a1a 50%,#000 100%);text-align:center;color:#fff}
  .headline h1{font-family:"Russo One",sans-serif;font-size:38px;font-weight:400;margin-top:10px;letter-spacing:1px}
  .headline h1 .accent{color:var(--yellow)}
  .headline .specialty{font-family:"Russo One",sans-serif;font-size:26px;margin-top:2px;letter-spacing:1px}
  .headline .promise{font-family:"Roboto",sans-serif;font-size:31px;color:var(--yellow);margin-top:4px}
  .band{position:absolute;left:0;width:870px;text-align:center}
  .band-depend{top:809px;height:71px;background:var(--mist)}
  .band-depend p{font-size:20px;margin-top:8px}
  .band-depend .service{font-family:"Russo One",sans-serif;font-size:16px;color:var(--gold);margin-top:9px;letter-spacing:1px}
  .band-clients{top:880px;height:43px;background:var(--paper);font-size:16.5px;line-height:43px}
  .band-clients .sep{color:var(--gold);margin:0 4px}
  .band-needs{top:923px;height:78px;background:var(--mist)}
  .band-needs h2{font-size:19.5px;font-weight:700;color:var(--gold);margin-top:10px}
  .band-needs p{font-size:19.5px;margin-top:6px}
  .simple{position:absolute;left:30px;top:1020px;width:400px;text-align:center;font-weight:700;font-size:16.5px;line-height:21px;color:#222}
  .accreditation{position:absolute;left:561px;top:1010px;width:108px;height:42px;background:var(--badge);border-radius:4px}
  .listing{position:absolute;left:706px;top:1018px;font-family:"Lato",sans-serif;font-weight:700;font-size:21px;color:#222}
  .footer{position:absolute;left:0;top:1058px;width:870px;height:67px}
  .call{position:absolute;left:38px;top:1080px;font-size:20px;color:#fff;display:flex;align-items:center;gap:10px}
  .call svg{width:18px;height:18px}
  .web{position:absolute;left:384px;top:1083px;font-size:16.5px;color:#fff;letter-spacing:2.4px}
  .follow{position:absolute;left:708px;top:1063px;font-family:"Roboto Condensed",sans-serif;font-size:15.5px;color:var(--yellow)}
  .social{position:absolute;left:722px;top:1090px;display:flex;gap:3px}
  .social span{width:17px;height:17px;background:var(--yellow)}
</style>
</head>
<body>
<div class="flyer">
  <div class="brand">
    <div class="brand-square"></div>
    <div class="brand-name"><span class="main">KESTREL</span><span class="sub">PELLMAN HAULERS</span></div>
  </div>

  <svg class="collage" viewBox="0 0 870 543" preserveAspectRatio="none" xmlns="http://www.w3.org/2000/svg">
    <defs>
      <linearGradient id="sky" x1="0" y1="0" x2="0" y2="1"><stop offset="0" stop-color="#7fb6e4"/><stop offset="1" stop-color="#5b6a78"/></linearGradient>
      <linearGradient id="roof" x1="0" y1="0" x2="0" y2="1"><stop offset="0" stop-color="#8fc0ea"/><stop offset=".5" stop-color="#6d6470"/><stop offset="1" stop-color="#6a9a3c"/></linearGradient>
      <linearGradient id="trailers" x1="0" y1="0" x2="0" y2="1"><stop offset="0" stop-color="#4f9be0"/><stop offset="1" stop-color="#1b1d24"/></linearGradient>
      <linearGradient id="logs" x1="0" y1="0" x2="0" y2="1"><stop offset="0" stop-color="#a39f94"/><stop offset="1" stop-color="#2a2c31"/></linearGradient>
      <linearGradient id="yard" x1="0" y1="0" x2="0" y2="1"><stop offset="0" stop-color="#b8a46a"/><stop offset="1" stop-color="#5f6b3c"/></linearGradient>
      <linearGradient id="shingle" x1="0" y1="0" x2="1" y2="1"><stop offset="0" stop-color="#9a9ea6"/><stop offset="1" stop-color="#3b3f46"/></linearGradient>
      <linearGradient id="cleanout" x1="0" y1="0" x2="0" y2="1"><stop offset="0" stop-color="#8aa3c4"/><stop offset=".5" stop-color="#2f8a4a"/><stop offset="1" stop-color="#8a8c6a"/></linearGradient>
      <linearGradient id="grey" x1="0" y1="0" x2="1" y2="1"><stop offset="0" stop-color="#b8b8b8"/><stop offset="1" stop-color="#7a7a7a"/></linearGradient>
    </defs>
    <g role="img" aria-label="Workers climbing a ladder on a house wall, black and white"><polygon points="0,0 158,0 2,543 0,543" fill="url(#grey)"/></g>
    <g role="img" aria-label="Multi-storey building under construction"><polygon points="174,0 539,0 480,223 110,223" fill="url(#sky)"/></g>
    <g role="img" aria-label="Crew reroofing a brick house with a dump trailer on the lawn"><polygon points="556,0 870,0 870,223 494,223" fill="url(#roof)"/></g>
    <g role="img" aria-label="Row of black dump trailers under a blue sky"><polygon points="103,230 588,230 549,379 55,379" fill="url(#trailers)"/></g>
    <g role="img" aria-label="Dump trailer loaded with cut tree logs"><polygon points="599,230 870,230 870,379 556,379" fill="url(#logs)"/></g>
    <g role="img" aria-label="Workers carrying lumber across a yard"><polygon points="52,389 282,389 246,543 5,543" fill="url(#yard)"/></g>
    <g role="img" aria-label="Roofer in safety vest on a shingled roof"><polygon points="292,389 545,389 506,543 251,543" fill="url(#shingle)"/></g>
    <g role="img" aria-label="Family loading a green roll-off dumpster during a clean out"><polygon points="550,389 866,389 866,543 506,543" fill="url(#cleanout)"/></g>
  </svg>

  <div class="services">
    Residential / Commercial<span class="dot">•</span>Construction Jobsites<span class="dot">•</span>Residential Remodels<span class="dot">•</span>Clean Outs / Foreclosures<span class="dot">•</span>Yard Waste Removal<br>
    Weekly / Daily Services<span class="dot">•</span>Dump Trailers / Roll Offs<span class="dot">•</span>Serving Atlanta and surrounding areas
  </div>

  <div class="headline">
    <h1><span class="accent">ROOFING</span> PROJECT ?</h1>
    <div class="specialty">Our specialty...</div>
    <div class="promise">MULTIPLE ROOFS IN 1 DAY ? NO PROBLEM</div>
  </div>

  <div class="band band-depend">
    <p>You can depend on Kestrel to be there for you on time:</p>
    <div class="service">For Delivery and Pick up</div>
  </div>

  <div class="band band-clients">
    Contractors<span class="sep">-</span> Roofing companies<span class="sep">-</span>Business owners<span class="sep">-</span>Homeowners we can work
  </div>

  <div class="band band-needs">
    <h2>EXCLUSIVELY WITH YOU TO FIT YOUR NEEDS</h2>
    <p>whether you need weekly services, daily or just need us 1 time, No problem</p>
  </div>

  <p class="simple">We make it simple just call for your next project<br>or visit us online</p>
  <div class="accreditation" role="img" aria-label="QTC accredited business badge"></div>
  <div class="listing">Wendo board</div>

  <svg class="footer" viewBox="0 0 870 67" xmlns="http://www.w3.org/2000/svg">
    <polygon points="366,2 870,2 870,67 330,67" fill="var(--black)"/>
    <polygon points="0,15 362,15 336,56 0,56" fill="var(--gold)"/>
    <polygon points="0,56 336,56 332,60 0,60" fill="#f4f4f4"/>
  </svg>
  <div class="call">CALL NOW
    <svg viewBox="0 0 24 24" aria-hidden="true"><path fill="#fff" d="M6.6 10.8a15.1 15.1 0 0 0 6.6 6.6l2.2-2.2c.3-.3.7-.4 1-.2 1.1.4 2.3.6 3.6.6.6 0 1 .4 1 1V20c0 .6-.4 1-1 1A17 17 0 0 1 3 4c0-.6.4-1 1-1h3.5c.6 0 1 .4 1 1 0 1.3.2 2.5.6 3.6.1.3 0 .7-.2 1z"/></svg>
    555 314 2790</div>
  <div class="web">www.PellmanHaulers.example</div>
  <div class="follow">FOLLOW US ON</div>
  <div class="social" aria-hidden="true"><span></span><span></span><span></span><span></span></div>
</div>
</body>
</html>
```